design a construction company business card

Design business card around our logo. Card must have all the typical info: name, title, address, phone, email, business name, etc. Somewhere on the card I would like to see our motto "Built on integrity... Inspired by commitment." Consider adding a splash of bright orange to the card to complement the blues and silvers/grays in the logo. We are open to metallic inks, textures, etc. We would like to see options on both light and dark backgrounds. The font in the logo is Euro Technic Extended Regular.

```html
<!DOCTYPE html>
<html lang="en">
<head>
<meta charset="UTF-8">
<title>Halden Contracting, Inc. – Business Card</title>
<link href="https://fonts.googleapis.com/css2?family=Michroma&family=Orbitron:wght@700&display=swap" rel="stylesheet">
<style>
  :root {
    --backdrop: #2b2b2c;
    --card: #222223;
    --card-edge: #1a1a1b;
    --white: #f4f4f4;
    --silver: #b9bcc0;
    --blue: #2f7fd6;
    --blue-deep: #2a5fc4;
    --rule: #d8d8d8;
  }
  * { margin: 0; padding: 0; box-sizing: border-box; }
  html, body {
    width: 1200px;
    height: 901px;
    overflow: hidden;
    background: var(--backdrop);
  }
  .stage {
    position: relative;
    width: 1200px;
    height: 901px;
  }
  .card {
    position: absolute;
    left: 267px;
    width: 666px;
    height: 380px;
    background: var(--card);
    border: 1px solid var(--card-edge);
    box-shadow: 0 10px 26px rgba(0,0,0,.45);
  }
  .card--back { top: 48px; }
  .card--front { top: 470px; }

  /* Wordmark */
  .wordmark {
    display: flex;
    align-items: center;
    gap: 14px;
    font-family: "Michroma", sans-serif;
    white-space: nowrap;
  }
  .wordmark__square {
    width: 24px;
    height: 24px;
    flex: none;
  }
  .wordmark__name {
    font-size: 16px;
    letter-spacing: 1px;
    line-height: 1.35;
  }
  .wordmark__line { display: block; }

  /* Back side */
  .card--back .wordmark {
    position: absolute;
    left: 0; right: 0;
    top: 146px;
    justify-content: center;
  }
  .card--back .wordmark__square { background: var(--silver); }
  .card--back .wordmark__name { color: var(--silver); }
  .motto {
    position: absolute;
    left: 0; right: 0;
    bottom: 40px;
    text-align: center;
    font-family: "Michroma", sans-serif;
    font-size: 13px;
    letter-spacing: 1.2px;
    color: var(--blue);
  }

  /* Front side */
  .card--front .wordmark {
    position: absolute;
    left: 34px;
    top: 164px;
  }
  .card--front .wordmark__square { background: var(--blue-deep); }
  .card--front .wordmark__name { color: var(--blue-deep); }
  .divider {
    position: absolute;
    left: 360px;
    top: 98px;
    width: 2px;
    height: 176px;
    background: var(--rule);
  }
  .contact {
    position: absolute;
    left: 384px;
    top: 102px;
    font-family: "Michroma", sans-serif;
    color: var(--white);
  }
  .contact__name {
    font-family: "Orbitron", sans-serif;
    font-weight: 700;
    font-size: 24px;
    letter-spacing: 1px;
    line-height: 1.1;
  }
  .contact__title {
    font-size: 15px;
    color: var(--blue);
    margin-top: 4px;
  }
  .contact__list {
    list-style: none;
    margin-top: 16px;
  }
  .contact__item {
    position: relative;
    padding-left: 22px;
    font-size: 13px;
    line-height: 1.35;
    margin-bottom: 2px;
  }
  .contact__item svg {
    position: absolute;
    left: 0;
    top: 2px;
    width: 11px;
    height: 11px;
    fill: var(--blue);
  }
  .contact__item .accent { color: var(--blue); }
</style>
</head>
<body>
<main class="stage">

  <section class="card card--back" aria-label="Card back">
    <div class="wordmark">
      <span class="wordmark__square"></span>
      <span class="wordmark__name">
        <span class="wordmark__line">HALDEN</span>
        <span class="wordmark__line">CONTRACTING, INC.</span>
      </span>
    </div>
    <p class="motto">"Built on integrity... Inspired by commitment."</p>
  </section>

  <section class="card card--front" aria-label="Card front">
    <div class="wordmark">
      <span class="wordmark__square"></span>
      <span class="wordmark__name">
        <span class="wordmark__line">HALDEN</span>
        <span class="wordmark__line">CONTRACTING, INC.</span>
      </span>
    </div>
    <div class="divider"></div>
    <div class="contact">
      <h1 class="contact__name">DANIEL BROOKS</h1>
      <p class="contact__title">Ceo &amp; Founder</p>
      <ul class="contact__list">
        <li class="contact__item">
          <svg viewBox="0 0 12 12"><path d="M6 0a4 4 0 0 0-4 4c0 3 4 8 4 8s4-5 4-8a4 4 0 0 0-4-4zm0 5.5A1.5 1.5 0 1 1 6 2.5a1.5 1.5 0 0 1 0 3z"/></svg>
          Your Street Address,<br>UnitedStates, 1234
        </li>
        <li class="contact__item">
          <svg viewBox="0 0 12 12"><path d="M2.5 0.5l2 2.5-1.2 1.3a7 7 0 0 0 4.4 4.4L9 7.5l2.5 2-1.3 2C5.5 11.5.5 6.5.5 1.8z"/></svg>
          000 111 2223
        </li>
        <li class="contact__item">
          <svg viewBox="0 0 12 12"><path d="M0 2h12v8H0zm1 1v.4l5 3.3 5-3.3V3zm0 1.6V9h10V4.6L6 7.9z"/></svg>
          urname@email.com
        </li>
        <li class="contact__item">
          <svg viewBox="0 0 12 12"><circle cx="6" cy="6" r="5.5"/></svg>
          www.<span class="accent">ursitename</span>.com
        </li>
      </ul>
    </div>
  </section>

</main>
</body>
</html>
```